Need Business Card for our Indian Grocery Store

Industry/Entity Type

Grocery Store

Contact Information for Business Card

Manoj Baweja
Director

Store Locations:

Brackleigh
482 Elm Parade
P: 03 9172 5843

Fenwarden
613 Carlow Road
P: 03 9238 6014

email: kvtmarts@mailnest.example

Requirements
Must have
• Our logo Colours

```html
<!DOCTYPE html>
<html lang="en">
<head>
<meta charset="utf-8">
<title>KVT Marts Business Card</title>
<link rel="stylesheet" href="https://fonts.googleapis.com/css2?family=Libre+Baskerville:wght@400;700&display=swap">
<style>
  :root {
    --brand-red: #e01b22;
    --deep-red: #c8141a;
    --paper: #ffffff;
    --ink-grey: #555555;
    --backdrop: #e9e7e4;
  }
  html, body {
    margin: 0;
    padding: 0;
    width: 1200px;
    height: 1132px;
    overflow: hidden;
    background: var(--backdrop);
    font-family: "Libre Baskerville", Georgia, serif;
  }
  .canvas {
    position: relative;
    width: 1200px;
    height: 1132px;
  }
  .card {
    position: absolute;
    left: 180px;
    width: 840px;
    height: 480px;
    overflow: hidden;
    box-shadow: 0 6px 18px rgba(0,0,0,0.18);
  }
  .card-front { top: 60px; background: var(--brand-red); }
  .card-back { top: 592px; background: var(--brand-red); }

  .front-band {
    position: absolute;
    inset: 0;
    width: 840px;
    height: 480px;
  }
  .brand-name {
    position: absolute;
    font-weight: 700;
    letter-spacing: 1px;
    white-space: nowrap;
  }
  .card-front .brand-name {
    left: 56px;
    top: 96px;
    font-size: 46px;
    color: var(--brand-red);
  }
  .person {
    position: absolute;
    right: 60px;
    top: 54px;
    text-align: left;
  }
  .person-name {
    font-size: 30px;
    font-weight: 700;
    color: var(--brand-red);
    letter-spacing: 1px;
    text-transform: uppercase;
    margin: 0;
  }
  .person-role {
    font-size: 13px;
    color: var(--ink-grey);
    letter-spacing: 1.5px;
    margin: 6px 0 0;
    text-transform: uppercase;
  }
  .locations {
    position: absolute;
    left: 56px;
    bottom: 48px;
    color: var(--paper);
    font-size: 15px;
    line-height: 1.65;
  }
  .locations p { margin: 0; }
  .locations .store { margin-top: 14px; }
  .locations strong { font-weight: 700; }
  .email {
    position: absolute;
    right: 56px;
    bottom: 150px;
    color: var(--paper);
    font-size: 15px;
    display: flex;
    align-items: center;
    gap: 10px;
  }
  .email-icon { width: 18px; height: 18px; flex: none; }

  .card-back .brand-mark {
    position: absolute;
    left: 50%;
    top: 50%;
    transform: translate(-50%, -50%);
    display: flex;
    align-items: center;
    gap: 18px;
  }
  .brand-square {
    width: 22px;
    height: 22px;
    background: var(--paper);
  }
  .card-back .brand-name {
    position: static;
    font-size: 56px;
    color: var(--paper);
  }
</style>
</head>
<body>
<main class="canvas">
  <section class="card card-front" aria-label="Business card front">
    <svg class="front-band" viewBox="0 0 840 480" aria-hidden="true">
      <path d="M0 0 H840 V170 Q420 240 0 265 Z" fill="var(--paper)"/>
    </svg>
    <div class="brand-name">KVT Marts</div>
    <div class="person">
      <p class="person-name">Manoj Baweja</p>
      <p class="person-role">Director</p>
    </div>
    <div class="locations">
      <p><strong>Store Locations :</strong> Brackleigh, 482 Elm Parade</p>
      <p><strong>P :</strong> 03 9172 5843</p>
      <p class="store"><strong>Fenwarden :</strong> 613 Carlow Road</p>
      <p><strong>P :</strong> 03 9238 6014</p>
    </div>
    <div class="email">
      <svg class="email-icon" viewBox="0 0 18 18" aria-hidden="true">
        <circle cx="9" cy="9" r="9" fill="var(--paper)"/>
        <rect x="4.5" y="6" width="9" height="6.5" fill="none" stroke="var(--brand-red)" stroke-width="1.2"/>
        <path d="M4.5 6 L9 9.8 L13.5 6" fill="none" stroke="var(--brand-red)" stroke-width="1.2"/>
      </svg>
      <span>email: kvtmarts@mailnest.example</span>
    </div>
  </section>

  <section class="card card-back" aria-label="Business card back">
    <div class="brand-mark">
      <span class="brand-square" aria-hidden="true"></span>
      <span class="brand-name">KVT Marts</span>
    </div>
  </section>
</main>
</body>
</html>
```